Financial Sevices firm looking for Brochure design

Our company Dunmere Halcott and Vesk Limited (DunmereVesk)
i
Is an investment/advisory firm - www.dunmerevesk.com
We invest in the energy sector in Africa and offer advisory services to Energy companies looking to invest in Africa. From oil and gas, to renewables (wind/solar). We are more focused on the "West African" Sub region
We need corporate brochure (Booklet style) to circulate to our corporate clients
We would like to see a design that considers the colours in our Logo (see website)
HI Guys, sorry been travelling. Seen some very good submissions and will be sending updates shortly
Reason: Dear Designers,
Thank you for participating in this project and for some of the great designs i've received so far. Unfortunately, due to the holidays, it has been difficult to consult with other members of my team. As a result, the project deadline is extended by about 12 days
I appreciate your understanding in the situation and looking forward to continuing the excellent collaboration in the coming days
Reason: Hi All,
Apologies for the multiple deadline extensions and thanks so much for all the designs which my team and I will be reviewing today and tomorrow.
We will be closing this project tomorrow by 6pm GMT (17th Jan 2014)
Thanks to all those that submitted such wonderful designs and goodluck!!
Project to be closed finally on 17th Jan 2014 at 6pm GMT
Banks, Investment Firms, Energy companies, Private Equity Funds
I have attached a Brochure that I created myself as an example of the type of information required but please also feel free to visit our website www.dunmerevesk.com
Looking for any creative ideas you have to suplement the information provided.
Financial

```html
<!DOCTYPE html>
<html lang="en">
<head>
<meta charset="utf-8">
<title>DunmereVesk — Vision, Mission and Values Spread</title>
<link rel="stylesheet" href="https://fonts.googleapis.com/css2?family=Archivo+Black&family=Arimo:wght@400&family=Raleway:wght@300&display=swap">
<style>
  :root {
    --red: #fb0000;
    --red-deep: #9e1111;
    --red-veil: rgba(214, 30, 30, 0.82);
    --ink: #0a0a0c;
    --slate: #3f4a4a;
    --paper: #ffffff;
    --text-dark: #222222;
    --text-light: #f3dede;
  }
  * { box-sizing: border-box; margin: 0; padding: 0; }
  html, body { width: 1200px; height: 1000px; overflow: hidden; background: var(--paper); }
  .canvas { position: relative; width: 1200px; height: 1000px; background: var(--paper); }

  .page {
    position: absolute; top: 136px; width: 516px; height: 728px; overflow: hidden;
    box-shadow: 0 6px 22px rgba(0,0,0,0.28);
  }

  /* Left page: vision & mission */
  .page--vision { left: 68px; background: var(--ink); }
  .page--vision .top-band { position: absolute; left: 0; top: 0; width: 516px; height: 24px; background: var(--red); }
  .page--vision .top-band__tab { position: absolute; left: 0; top: 0; width: 60px; height: 24px; background: #1b1b1b; }
  .plant-photo {
    position: absolute; left: 0; top: 24px; width: 516px; height: 462px;
    background: linear-gradient(180deg, #6e6e6e 0%, #b9b9b9 38%, #8a8a8a 62%, #2a2a2a 100%);
  }
  .statement-panel {
    position: absolute; left: 50px; top: 379px; width: 420px; height: 283px;
    background: linear-gradient(180deg, var(--red-veil) 0 105px, var(--red-deep) 105px);
  }
  .statement-label {
    position: absolute; left: 0; height: 38px; padding: 0 20px;
    background: var(--ink); color: #fff;
    font: 300 22px/38px "Raleway", sans-serif;
  }
  .statement-label--vision { top: 30px; }
  .statement-label--mission { top: 151px; }
  .statement-text {
    position: absolute; left: 18px; color: var(--text-light);
    font: 400 13.5px/21px "Arimo", sans-serif;
  }
  .statement-text--vision { top: 76px; width: 310px; }
  .statement-text--mission { top: 200px; width: 352px; }

  /* Right page: values */
  .page--values { left: 616px; background: var(--paper); }
  .values-heading {
    position: absolute; left: 69px; top: 111px; color: var(--text-dark);
    font: 300 21px/28px "Raleway", sans-serif; letter-spacing: 0.5px; word-spacing: 4px;
  }
  .team-photo {
    position: absolute; left: 264px; top: 39px; width: 246px; height: 106px;
    background: linear-gradient(180deg, rgba(251,0,0,0.15) 0%, rgba(251,0,0,0.85) 100%);
  }
  .tower-photo {
    position: absolute; left: 0; top: 145px; width: 456px; height: 495px;
    background: linear-gradient(125deg, #d8d8d8 0%, #5a5a5a 30%, #a9a9a9 55%, #2c2c2c 100%);
  }
  .values-block { position: absolute; left: 60px; top: 145px; width: 456px; height: 467px; background: var(--red); }
  .values-words { position: absolute; left: 0; top: 0; }
  .values-words text { font-family: "Archivo Black", sans-serif; fill: url(#steel); stroke: rgba(255,255,255,0.55); stroke-width: 1; }
  .bottom-band { position: absolute; left: 60px; bottom: 0; width: 456px; height: 24px; background: var(--red); }
  .bottom-band__tab { position: absolute; left: 0; bottom: 0; width: 60px; height: 24px; background: var(--slate); }
</style>
</head>
<body>
<div class="canvas">

  <section class="page page--vision">
    <div class="top-band"></div>
    <div class="top-band__tab"></div>
    <div class="plant-photo" role="img" aria-label="Black and white photograph of pipework at an energy processing plant"></div>
    <div class="statement-panel">
      <h2 class="statement-label statement-label--vision">Our VISION</h2>
      <p class="statement-text statement-text--vision">To contribute to the implementation of robust infrastructure towards enhanced socio-economic development in Africa.</p>
      <h2 class="statement-label statement-label--mission">Our MISSION</h2>
      <p class="statement-text statement-text--mission">To create the greatest value for our clients and investors through the efficient implementation of infrastructure and energy related projects across Africa.</p>
    </div>
  </section>

  <section class="page page--values">
    <h2 class="values-heading">OUR VALUES</h2>
    <div class="team-photo" role="img" aria-label="Red image of a group of business people standing together"></div>
    <div class="tower-photo" role="img" aria-label="Black and white photograph of a glass office tower"></div>
    <div class="values-block"></div>
    <svg class="values-words" width="516" height="728" viewBox="0 0 516 728" aria-label="Integrity, Accountability, Respect, Teamwork">
      <defs>
        <linearGradient id="steel" x1="0" y1="0" x2="1" y2="1">
          <stop offset="0" stop-color="#e6e6e6"/>
          <stop offset="0.35" stop-color="#8c8c8c"/>
          <stop offset="0.6" stop-color="#3a3a3a"/>
          <stop offset="1" stop-color="#1e1e1e"/>
        </linearGradient>
      </defs>
      <text x="106" y="252" font-size="57" textLength="320" lengthAdjust="spacingAndGlyphs">INTEGRITY</text>
      <text x="106" y="299" font-size="48" textLength="320" lengthAdjust="spacingAndGlyphs">ACCOUNTABILITY</text>
      <text x="106" y="361" font-size="70" textLength="320" lengthAdjust="spacingAndGlyphs">RESPECT</text>
      <text x="106" y="482" font-size="146" textLength="320" lengthAdjust="spacingAndGlyphs">TEAM</text>
      <text x="106" y="594" font-size="139" textLength="320" lengthAdjust="spacingAndGlyphs">WORK</text>
    </svg>
    <div class="bottom-band"></div>
    <div class="bottom-band__tab"></div>
  </section>

</div>
</body>
</html>
```